Venture Traps Book Needs a Cover Design

We need a cover design for Venture Traps, Plain Guidance for Wobbly New Ventures and Stalled Company Founders. We will publish and ebook first (first priority), followed by a hard cover printed book, and then a soft cover book after a few months. The book includes 40 Venture Traps and actions owners can implement to counter them and grow. Some examples of killers: self-sabotage, wild optimism, scamming, addictions, burnout, no plan, procrastination, recklessness, haemorrhaging money, etc. We plan to publish the ebook to Readlo / Vendora standards. We want to see designs that convey professionalism, simplicity and creativity.

Target Market(s)

Small and microbusinesses, including start-ups, proprietorships, cottage industries, home-based, single operator, and businesses with or without employees, including corporations and partnerships with fewer than five employees

Industry/Entity Type

Business

Font styles to use
Sans Serif

Colors

Designer to choose colors to be used in the design.

Requirements
Must have
• Uncluttered, professional
• Title: Venture Traps
• Subtitle: Plain Guidance for Wobbly New Ventures and Stalled Company Founders
• Author: Miles Farquist
Nice to have
• n/a

```html
<!DOCTYPE html>
<html lang="en">
<head>
<meta charset="utf-8">
<title>Venture Traps — Book Cover</title>
<link rel="stylesheet" href="https://fonts.googleapis.com/css2?family=Montserrat:wght@700;800;900&display=swap">
<style>
  :root {
    --sky-top: #dfe8ee;
    --sky-mid: #f3f6f8;
    --cloud: #e9eef2;
    --ice: #dfe9ef;
    --title: #5d98b1;
    --title-light: #86b6c9;
    --title-deep: #4a86a1;
    --subtitle: #2f3336;
    --frame: #eeeff0;
    --wall: #b9bcbe;
    --interior: #2a2b2c;
  }
  * { margin: 0; padding: 0; box-sizing: border-box; }
  html, body { width: 750px; height: 1200px; overflow: hidden; background: #fff; }
  .cover {
    position: relative;
    width: 750px;
    height: 1200px;
    overflow: hidden;
    font-family: "Montserrat", sans-serif;
  }
  .backdrop {
    position: absolute;
    inset: 0;
    background:
      radial-gradient(ellipse 60% 6% at 30% 39%, var(--cloud) 0%, transparent 100%),
      radial-gradient(ellipse 55% 5% at 78% 36%, #f7f9fa 0%, transparent 100%),
      linear-gradient(180deg, var(--sky-top) 0%, var(--sky-mid) 22%, #fbfcfd 34%, #e6ecf0 42%, var(--ice) 60%, #eef3f6 100%);
  }
  .title {
    position: absolute;
    top: 52px;
    left: 0;
    width: 100%;
    text-align: center;
    font-weight: 900;
    font-size: 124px;
    line-height: 120px;
    letter-spacing: 3px;
    text-transform: uppercase;
    color: var(--title);
    background: linear-gradient(160deg, var(--title-light) 0%, var(--title) 45%, var(--title-deep) 100%);
    -webkit-background-clip: text;
    background-clip: text;
    -webkit-text-fill-color: transparent;
  }
  .subtitle {
    position: absolute;
    top: 348px;
    left: 55px;
    width: 640px;
    text-align: center;
    font-weight: 800;
    font-size: 18px;
    line-height: 30px;
    text-transform: uppercase;
    color: var(--subtitle);
  }
  .box-photo {
    position: absolute;
    left: 66px;
    top: 516px;
    width: 624px;
    height: 616px;
    background:
      radial-gradient(ellipse 45% 45% at 50% 50%, var(--interior) 0%, #3c3d3e 55%, var(--wall) 85%, var(--frame) 100%);
    box-shadow: 0 2px 6px rgba(0, 0, 0, 0.12);
  }
  .author {
    position: absolute;
    top: 1150px;
    left: 0;
    width: 100%;
    text-align: center;
    font-weight: 800;
    font-size: 20px;
    letter-spacing: 3px;
    text-transform: uppercase;
    color: var(--subtitle);
  }
</style>
</head>
<body>
<main class="cover">
  <div class="backdrop" role="img" aria-label="Soft sky with a band of clouds above a pale icy ground"></div>

  <h1 class="title">Venture<br>Traps</h1>

  <p class="subtitle">Plain Guidance for Wobbly New Ventures and Stalled Company Founders</p>

  <div class="box-photo" role="img" aria-label="Photo of a businessman in a dark suit crouching inside a white open box, pushing against its walls"></div>

  <p class="author">Miles Farquist</p>
</main>
</body>
</html>
```